ridge-mosaic builders & interiors

I need a web design for my company we offer counter tops. tile for floors,showers,kitchen backsplashes and more also need a place where the client
can write reviews

Industry/Entity Type

Tile

```html
<!DOCTYPE html>
<html lang="en">
<head>
<meta charset="utf-8">
<title>Ridge-Mosaic Builders &amp; Interiors</title>
<link href="https://fonts.googleapis.com/css2?family=Cinzel:wght@400;700&family=Marcellus&family=Open+Sans:ital,wght@0,400;0,600;1,400&display=swap" rel="stylesheet">
<style>
:root{
  --teal:#5fd0dc;
  --teal-dark:#3fbfcd;
  --teal-text:#2eb4c4;
  --orange:#f5a000;
  --nav:#1b1b1b;
  --nav-line:#3a3a3a;
  --text:#555;
  --heading:#222;
  --footer:#2b2b2b;
  --page:#ffffff;
}
*{margin:0;padding:0;box-sizing:border-box}
html,body{width:1041px;height:1200px;overflow:hidden}
body{position:relative;background:var(--page);font-family:"Open Sans",Arial,sans-serif;color:var(--text)}
.header-band{position:absolute;left:0;top:0;width:1041px;height:263px;background:linear-gradient(180deg,#6ad7e2 0%,#55cbd8 60%,#3fbccb 100%);border-bottom:1px solid #39a9b7}
.brand{position:absolute;left:89px;top:32px;font-family:"Marcellus",serif;font-size:28px;color:#fff;letter-spacing:.5px}
.phone{position:absolute;right:94px;top:31px;text-align:right;line-height:1}
.phone-label{font-size:15px;color:#1f1f1f}
.phone-number{font-size:23px;color:#fff;margin-top:5px}
.page{position:absolute;left:84px;top:138px;width:871px;height:958px;background:#fff;box-shadow:0 0 12px rgba(0,0,0,.08)}
.nav{position:absolute;left:84px;top:93px;width:873px;height:45px;display:flex;background:linear-gradient(#2a2a2a,#111);border-radius:3px 3px 0 0;overflow:hidden}
.nav a{display:flex;align-items:center;justify-content:center;color:#fff;text-decoration:none;font-size:13px;border-left:1px solid var(--nav-line)}
.nav a:first-child{border-left:none}
.nav a.active{background:linear-gradient(#fff,#ececec);color:#1d1d1d}
.slider{position:absolute;left:89px;top:143px;width:863px;height:326px;background:linear-gradient(160deg,#b9c6c4 0%,#d8c7a6 35%,#c8a77a 55%,#4a2f22 80%,#2e1d16 100%);overflow:hidden}
.slide-caption{position:absolute;left:0;right:0;top:111px;text-align:center;font-family:"Cinzel",serif;color:#2a2118}
.slide-title{font-size:30px;font-weight:700;line-height:1}
.slide-sub{font-size:21px;margin-top:6px}
.slide-arrow{position:absolute;top:118px}
.slide-arrow.prev{left:17px}
.slide-arrow.next{right:17px}
.dots{position:absolute;left:412px;top:300px;display:flex;gap:4px}
.dots span{width:10px;height:10px;border-radius:50%;background:#fff}
.dots span.on{background:var(--teal-dark)}
.features{position:absolute;left:83px;top:473px;width:873px;height:219px;border:1px solid #e2e2e2;border-radius:3px;background:linear-gradient(#fff 60%,#f4f4f4)}
.feature{position:absolute;top:17px;width:200px}
.feature-img{width:200px;height:108px;border:1px solid #d8d8d8}
.feature h3{font-weight:400;font-size:17px;color:var(--teal-text);margin:9px 0 0 2px;line-height:1.2}
.feature p{font-size:10.5px;line-height:16.5px;margin:3px 0 0 4px}
.welcome{position:absolute;left:106px;top:722px;width:552px}
.welcome h1{font-weight:400;font-size:22px;color:var(--heading);line-height:1.2}
.welcome p{font-size:11.3px;line-height:19.7px;margin-top:5px}
.divider{position:absolute;left:105px;top:880px;width:547px;border-top:1px solid #d6d6d6}
.services{position:absolute;left:108px;top:897px;width:560px}
.services h2{font-weight:400;font-size:18px;color:var(--teal-text)}
.service-list{list-style:none;display:grid;grid-template-columns:260px 260px;row-gap:5.5px;margin-top:12px}
.service-list li{font-size:10.6px;display:flex;align-items:center;gap:6px;height:16px}
.testimonials{position:absolute;left:685px;top:722px;width:260px}
.testimonials h2{font-weight:600;font-size:19px;color:var(--orange)}
.review{position:absolute;left:4px;width:256px}
.review-photo{position:absolute;left:0;top:0;width:63px;height:55px;border:1px solid #ddd}
.review-body{position:absolute;left:74px;top:-4px;width:182px;font-size:9.8px;line-height:16.4px;font-style:italic;color:#666}
.review-author{font-style:normal;font-weight:600;color:#555;margin-top:2px}
.footer{position:absolute;left:0;top:1096px;width:1041px;height:104px;background:var(--footer)}
.footer-nav{position:absolute;left:108px;top:25px;font-size:12.4px;color:#fff}
.footer-nav span{margin:0 6px}
.copyright{position:absolute;left:108px;top:51px;font-size:9.8px;color:#ddd}
.social{position:absolute;left:838px;top:23px;display:flex;gap:3.5px}
.social span{width:23px;height:23px;border-radius:50%;background:#fff}
</style>
</head>
<body>
<div class="header-band"></div>
<div class="brand">Ridge-Mosaic Builders &amp; Interiors</div>
<div class="phone">
  <div class="phone-label">Phone Support</div>
  <div class="phone-number">(555) 204-7318</div>
</div>

<div class="page"></div>

<nav class="nav">
  <a class="active" style="width:89px">HOME</a>
  <a style="width:99px">ABOUT US</a>
  <a style="width:155px">LATEST PRODUCTS</a>
  <a style="width:93px">SERVICES</a>
  <a style="width:128px">TESTIMONIALS</a>
  <a style="width:90px">SUPPORT</a>
  <a style="width:96px">GALLERY</a>
  <a style="width:123px">CONTACT US</a>
</nav>

<section class="slider" role="img" aria-label="Photo of a bathroom vanity with a cream travertine stone countertop and dark wood cabinets">
  <div class="slide-caption">
    <div class="slide-title">Floor Tiles &amp; Kitchen Backsplashes</div>
    <div class="slide-sub">Mauris vel lacus vitae felis vestibulum volutpat Etiam est</div>
  </div>
  <svg class="slide-arrow prev" width="24" height="62" viewBox="0 0 24 62"><polyline points="22,1 2,31 22,61" fill="none" stroke="#fff" stroke-width="1.5"/></svg>
  <svg class="slide-arrow next" width="24" height="62" viewBox="0 0 24 62"><polyline points="2,1 22,31 2,61" fill="none" stroke="#fff" stroke-width="1.5"/></svg>
  <div class="dots"><span class="on"></span><span></span><span></span></div>
</section>

<section class="features">
  <article class="feature" style="left:20px">
    <div class="feature-img" role="img" aria-label="Photo of a granite counter top on a dark cabinet" style="background:linear-gradient(#dfe6d6 0%,#cfd8c4 55%,#8a6a4a 62%,#2b2a2a 80%)"></div>
    <h3>Counter tops</h3>
    <p>Aliquam nec erat at purus cursus inter-dum Vestibulum ligula augue biben</p>
  </article>
  <article class="feature" style="left:230px">
    <div class="feature-img" role="img" aria-label="Photo of a veined marble slab for floor tiles" style="background:linear-gradient(135deg,#8f9692,#5d6461 50%,#9aa09c)"></div>
    <h3>Floor Tiles</h3>
    <p>Aliquam nec erat at purus cursus inter-dum Vestibulum ligula augue biben</p>
  </article>
  <article class="feature" style="left:440px">
    <div class="feature-img" role="img" aria-label="Photo of a rain shower head with running water" style="background:radial-gradient(circle at 50% 35%,#d9d4c8 0%,#b38a4a 35%,#a85a10 70%,#7a3a08 100%)"></div>
    <h3>Showers</h3>
    <p>Aliquam nec erat at purus cursus inter-dum Vestibulum ligula augue biben</p>
  </article>
  <article class="feature" style="left:650px">
    <div class="feature-img" role="img" aria-label="Photo of a tiled kitchen backsplash above a granite counter" style="background:linear-gradient(#d8c09a 0%,#c9ab7e 60%,#8b6a46 100%)"></div>
    <h3>Kitchen Backsplashes</h3>
    <p>Aliquam nec erat at purus cursus inter-dum Vestibulum ligula augue biben</p>
  </article>
</section>

<section class="welcome">
  <h1>Welcome to Ridge-Mosaic Builders Homepage</h1>
  <p>Suspendisse vulputate aliquam dui Nulla elementum dui ut augue Aliquam vehicula mi at mauris Maecenas placerat nisl at consequat rhoncus sem nunc gravida justo quis eleifend arcu velit quis lacus Morbi magna magna tincidunt a mattis non imperdiet vitae tellus Sed odio est auctor ac sollicitudin in consequat vitae orci</p>
  <p>Suspendisse vulputate aliquam dui Nulla elementum dui ut augue Aliquam vehicula mi at mauris Maecenas placerat nisl at consequat rhoncus sem nunc gravida justo quis eleifend arcu velit quis lacus</p>
</section>
<div class="divider"></div>

<section class="services">
  <h2>Services We Provide</h2>
  <ul class="service-list">
    <li><svg width="13" height="11" viewBox="0 0 13 11"><path d="M1 6 L5 10 L12 1" fill="none" stroke="#2eb4c4" stroke-width="2.4"/></svg>Nunc tempus felis vitae urna Vivamus</li>
    <li><svg width="13" height="11" viewBox="0 0 13 11"><path d="M1 6 L5 10 L12 1" fill="none" stroke="#2eb4c4" stroke-width="2.4"/></svg>Nunc tempus felis vitae urna Vivamus</li>
    <li><svg width="13" height="11" viewBox="0 0 13 11"><path d="M1 6 L5 10 L12 1" fill="none" stroke="#2eb4c4" stroke-width="2.4"/></svg>Curabitur iaculis tempus eros</li>
    <li><svg width="13" height="11" viewBox="0 0 13 11"><path d="M1 6 L5 10 L12 1" fill="none" stroke="#2eb4c4" stroke-width="2.4"/></svg>Curabitur iaculis tempus eros</li>
    <li><svg width="13" height="11" viewBox="0 0 13 11"><path d="M1 6 L5 10 L12 1" fill="none" stroke="#2eb4c4" stroke-width="2.4"/></svg>Curabitur vel mi sit amet magna malesuada</li>
    <li><svg width="13" height="11" viewBox="0 0 13 11"><path d="M1 6 L5 10 L12 1" fill="none" stroke="#2eb4c4" stroke-width="2.4"/></svg>Curabitur vel mi sit amet magna malesuada</li>
    <li><svg width="13" height="11" viewBox="0 0 13 11"><path d="M1 6 L5 10 L12 1" fill="none" stroke="#2eb4c4" stroke-width="2.4"/></svg>Fusce ultricies orci</li>
    <li><svg width="13" height="11" viewBox="0 0 13 11"><path d="M1 6 L5 10 L12 1" fill="none" stroke="#2eb4c4" stroke-width="2.4"/></svg>Fusce ultricies orci</li>
  </ul>
</section>

<aside class="testimonials">
  <h2>Customer Testimonials</h2>
  <div class="review" style="top:36px">
    <div class="review-photo" role="img" aria-label="Customer portrait" style="background:linear-gradient(#e9e6e2,#c9a88c)"></div>
    <div class="review-body">Etiam est nunc venenatis in tristique eu imperdiet ac nisl Cum sociis natoque pe-natibus et magnis dis parturient montes nascetur ridiculus mus In iaculis
      <div class="review-author">By Author name</div></div>
  </div>
  <div class="review" style="top:130px">
    <div class="review-photo" role="img" aria-label="Customer portrait" style="background:linear-gradient(#5f7a3e,#b08a6a)"></div>
    <div class="review-body">Etiam est nunc venenatis in tristique eu imperdiet ac nisl Cum sociis natoque pe-natibus et magnis dis parturient montes nascetur ridiculus mus In iaculis
      <div class="review-author">By Author name</div></div>
  </div>
  <div class="review" style="top:223px">
    <div class="review-photo" role="img" aria-label="Customer portrait" style="background:linear-gradient(#c9b38a,#3a5a9a)"></div>
    <div class="review-body">Imperdiet ac nisl Cum sociis natoque pe-natibus et magnis dis parturient montes nascetur ridiculus mus In iaculis
      <div class="review-author">By Author name</div></div>
  </div>
</aside>

<footer class="footer">
  <div class="footer-nav">HOME<span>|</span>ABOUT US<span>|</span>LATEST PRODUCTS<span>|</span>SERVICES<span>|</span>TESTIMONIALS<span>|</span>SUPPORT<span>|</span>GALLERY<span>|</span>CONTACT US</div>
  <div class="copyright">© 2014 Company Name.&nbsp; All right reserved.&nbsp; Term of Use</div>
  <div class="social" aria-label="Social links"><span></span><span></span><span></span><span></span></div>
</footer>
</body>
</html>
```